Donor Thank You Card – Evelyn’s Harbor Pregnancy & Family Support

Project Overview:
We are seeking a heartfelt, beautifully designed thank-you card for our nonprofit, Evelyn’s Harbor Pregnancy & Family Support. This card will be sent to donors as a tangible expression of gratitude from Evelyn’s family.

The design should feel warm, personal, and meaningful—something a recipient would want to keep.

About the Organization
Evelyn’s Harbor Pregnancy & Family Support exists to support families navigating complicated pregnancies, prolonged hospital stays, and loss.
The organization was created in honor of Evelyn, and everything we do is centered around providing comfort, connection, and a “web of care” during life’s most difficult moments.

Design Objective
Create a thank-you card that conveys:
-Deep gratitude
-Compassion and warmth
-A sense of connection and care
Subtle remembrance and hope
-This should feel personal and heartfelt—not corporate or transactional.

Color Palette: Neutrals (cream, soft beige, warm white)
Soft pastels (blush, sage, muted gold, light blue)
Avoid anything too bold or high contrast

Visual Elements:
Subtle “web” motif (very delicate—not literal or harsh)
Soft sunlight / glow elements (“little sunshine” theme)
Organic textures (linen, paper grain, watercolor feel)
Minimalist line illustrations

Card Format
Standard folded card (5x7 preferred)
Front + inside spread
Front of Card (Minimal + Elegant)

Option 1:
Evelyn’s Harbor logo
Short phrase:
“With gratitude”

Option 2:
Logo + subtle design element (sunlight/web texture)
No text or very minimal text

Inside of Card (Main Message)
Include this message:
Because of you, a family will feel supported during one of the most difficult moments of their lives.

Your generosity helps us provide comfort, care, and connection to families navigating complicated pregnancies, prolonged hospital stays, and loss.

From the bottom of our hearts, thank you for being part of this web of support.

With gratitude,
Evelyn’s Family

Back of Card:
Logo: (See attachments)
Website URL: www.evelynsharborsupport.org
Small tagline: “Woven with care, held with hope, and touched by a little sunshine.”

Let me know if you need any other variations of the logo.

Thank you!

```html
<!DOCTYPE html>
<html lang="en">
<head>
<meta charset="utf-8">
<title>Evelyn’s Harbor – Donor Thank You Card</title>
<link href="https://fonts.googleapis.com/css2?family=Great+Vibes&family=Playfair+Display:ital,wght@0,400;0,600;1,400;1,600&display=swap" rel="stylesheet">
<style>
  :root {
    --backdrop: #efeef0;
    --paper-inner: #f7f4fa;
    --paper-cover: #fbf7f3;
    --paper-back: #ffffff;
    --ink: #3e3448;
    --plum: #8d6fae;
    --lilac: #b9a3d6;
    --gold: #c9a46b;
    --blush: #e9b9c3;
    --muted: #7d7486;
  }
  * { box-sizing: border-box; margin: 0; padding: 0; }
  html, body {
    width: 853px; height: 1200px; overflow: hidden;
    background: var(--backdrop);
  }
  .canvas {
    position: relative; width: 853px; height: 1200px;
  }
  .spread {
    position: absolute; left: 82px; width: 690px; height: 460px;
    display: flex;
  }
  .spread--inside { top: 110px; background: var(--paper-inner); }
  .spread--outside { top: 630px; background: var(--paper-back); }

  /* Inside spread */
  .inside-art {
    width: 345px; height: 100%;
    background:
      radial-gradient(ellipse 38% 42% at 64% 46%, #8f6fc7 0%, rgba(172,140,214,.7) 45%, rgba(247,244,250,0) 100%),
      radial-gradient(ellipse 34% 40% at 32% 40%, #b24a63 0%, rgba(219,128,145,.75) 45%, rgba(247,244,250,0) 100%),
      radial-gradient(ellipse 30% 24% at 70% 78%, rgba(158,120,206,.6) 0%, rgba(247,244,250,0) 100%),
      var(--paper-inner);
  }
  .inside-message {
    width: 345px; padding: 52px 40px 0 24px;
    font-family: "Playfair Display", Georgia, serif;
    font-style: italic; color: var(--ink);
    font-size: 13px; line-height: 1.55; text-align: center;
  }
  .inside-message p { margin-bottom: 16px; }
  .inside-message .sign-off { margin-top: 26px; }
  .inside-message .sign-name { font-weight: 600; }

  /* Outside spread */
  .back-panel {
    width: 345px; height: 100%;
    display: flex; flex-direction: column; align-items: center;
    padding-top: 255px;
    font-family: "Playfair Display", Georgia, serif;
  }
  .front-panel {
    width: 345px; height: 100%; position: relative;
    background: var(--paper-cover);
    display: flex; flex-direction: column; align-items: center; justify-content: center;
    font-family: "Playfair Display", Georgia, serif;
    border-left: 1px solid #eee7e2;
  }
  .front-frame {
    position: absolute; inset: 18px;
    border: 1px solid var(--gold); opacity: .7;
  }
  .front-frame::after {
    content: ""; position: absolute; inset: 5px;
    border: 1px solid var(--gold); opacity: .5;
  }
  .wordmark {
    color: var(--plum); font-weight: 400; text-align: center;
  }
  .wordmark--front { font-size: 34px; line-height: 1.15; }
  .wordmark--front .wordmark-sub { display: block; font-size: 16px; margin-top: 4px; }
  .wordmark--back { font-size: 19px; line-height: 1.15; }
  .wordmark--back .wordmark-sub { display: block; font-size: 9px; margin-top: 2px; }
  .wordmark-dot {
    width: 10px; height: 10px; border-radius: 50%;
    background: var(--lilac); margin-bottom: 8px;
  }
  .front-phrase {
    font-family: "Great Vibes", cursive;
    color: var(--gold); font-size: 34px; margin-top: 14px;
  }
  .tagline {
    font-style: italic; font-size: 9px; color: var(--muted);
    margin-top: 14px; text-align: center;
  }
  .website {
    font-size: 9px; color: var(--muted); margin-top: 44px; letter-spacing: .3px;
  }
</style>
</head>
<body>
<main class="canvas">

  <section class="spread spread--inside" aria-label="Inside of card">
    <div class="inside-art" role="img" aria-label="Watercolor butterfly with a delicate web among violet and pink flowers"></div>
    <div class="inside-message">
      <p>Because of you, a family will feel supported during one of the most difficult moments of their lives.</p>
      <p>Your generosity helps us provide comfort, care, and connection to families navigating complicated pregnancies, prolonged hospital stays, and loss.</p>
      <p>From the bottom of our hearts, thank you for being part of this web of support.</p>
      <p class="sign-off">With gratitude,<br><span class="sign-name">Evelyn’s Family</span></p>
    </div>
  </section>

  <section class="spread spread--outside" aria-label="Front and back of card">
    <div class="front-panel">
      <div class="front-frame"></div>
      <div class="wordmark-dot"></div>
      <h1 class="wordmark wordmark--front">Evelyn’s Harbor<span class="wordmark-sub">Pregnancy &amp; Family Support</span></h1>
      <p class="front-phrase">With gratitude</p>
    </div>
    <div class="back-panel">
      <div class="wordmark-dot"></div>
      <p class="wordmark wordmark--back">Evelyn’s Harbor<span class="wordmark-sub">Pregnancy &amp; Family Support</span></p>
      <p class="tagline">“Woven with care, held with hope, and touched by a little sunshine.”</p>
      <p class="website">www.evelynsharborsupport.org</p>
    </div>
  </section>

</main>
</body>
</html>
```